Stationery Design Project

Minimal Design. Black and White Colours Only.
Need Business Card
With Compliments slip
Letterhead
A4 Folder

Target Market(s)

Luxury architectual designed home owners

Industry/Entity Type

Business

Requirements
Must have
• Black and White colours only. Suggest some good textured stock for business card for future printing. try to use font that is used in my logo our some other minimal modern font.

```html
<!DOCTYPE html>
<html lang="en">
<head>
<meta charset="utf-8">
<title>Kiren Estates – With Compliments Slip</title>
<link rel="stylesheet" href="https://fonts.googleapis.com/css2?family=Archivo:wght@400;500&display=swap">
<style>
  :root {
    --backdrop: #e6e6e6;
    --paper: #ffffff;
    --ink: #000000;
    --ink-reverse: #ffffff;
  }
  * { margin: 0; padding: 0; box-sizing: border-box; }
  html, body {
    width: 1200px; height: 1000px; overflow: hidden;
    background: var(--backdrop);
    font-family: "Archivo", "Helvetica Neue", Arial, sans-serif;
  }
  .slip {
    position: absolute; left: 150px; top: 220px;
    width: 900px; height: 560px;
    background: var(--paper);
    box-shadow: 0 4px 14px rgba(0,0,0,0.18);
    overflow: hidden;
  }
  .brand {
    position: absolute; left: 470px; top: 96px;
    display: flex; align-items: center; gap: 18px;
    color: var(--ink);
  }
  .brand-square { width: 44px; height: 44px; background: var(--ink); }
  .brand-name {
    font-size: 38px; font-weight: 500; letter-spacing: 0.5px; line-height: 1;
  }
  .rule { position: absolute; height: 2px; background: var(--ink); }
  .rule-top { left: 60px; top: 178px; width: 390px; }
  .rule-bottom { left: 340px; top: 398px; width: 500px; }
  .greeting {
    position: absolute; left: 60px; top: 374px;
    font-size: 26px; font-weight: 400; letter-spacing: 0.5px; color: var(--ink);
  }
  .footer-band {
    position: absolute; left: 0; bottom: 0; width: 100%; height: 130px;
    background: var(--ink); color: var(--ink-reverse);
  }
  .address {
    position: absolute; left: 290px; top: 22px;
    font-size: 16px; letter-spacing: 0.4px;
  }
  .contacts {
    position: absolute; left: 290px; top: 52px;
    font-size: 10px; line-height: 14px; list-style: none;
  }
</style>
</head>
<body>
  <article class="slip">
    <div class="brand">
      <span class="brand-square"></span>
      <span class="brand-name">KIREN ESTATES</span>
    </div>
    <div class="rule rule-top"></div>
    <p class="greeting">With Compliments</p>
    <div class="rule rule-bottom"></div>
    <footer class="footer-band">
      <p class="address">Level 12, 48 Ridge St &nbsp;-&nbsp; Northvale QLD 4100 &nbsp;-&nbsp; Australia</p>
      <ul class="contacts">
        <li>M: +61 400 000 123</li>
        <li>P: +61 7 3000 0456</li>
        <li>E: hello@kirenestates.com</li>
      </ul>
    </footer>
  </article>
</body>
</html>
```